Corporate Design für Malermeister
Super Arbeit von dem ersten Entwurf an. Schnelle und präzise Umstzung von Änderungen. Durch tolle Vorschläge des Designers sowie meiner Vorstellung ist ein für mich perfektes und stimmiges Corparate Design entstanden. Die Zusammenarbeit war rundum ein voller Erfolg! Sehr zu empfehlen! Auch hier noch mal Danke für deine präzise und schnelle Arbeit. Mann merkt, dass hier mit einem Profi gearbeitet wird!
Zielgruppe
Ich bin Malermeister ,
wir bieten komplettrenovierungen an vom Gestalten der Oberflächen, kreative Wandgestaltung Trockenbau, Bodenverlegearbeiten Parkett, Laminat, Teppich, designböden etc.
Fokus liegt bei den Malerarbeiten! Auch Fassaden werden restaurariert und gestaltet
Wir wollen modern und hochwertig rüber kommen
Aufgabenstellung
Das Logo soll zeigen, dass wir ein moderner kreativer Betrieb sind
da wir eine Diesntaleistung anbieten sollte es auch auf Vertrauen asutrahlen

```html
<!DOCTYPE html>
<html lang="de">
<head>
<meta charset="utf-8">
<title>Farbraum – Visitenkarte Entwurf 01</title>
<link href="https://fonts.googleapis.com/css2?family=Roboto+Condensed:wght@700&family=Source+Sans+3:wght@300;400;600&display=swap" rel="stylesheet">
<style>
  :root {
    --frame-blue: #1070b8;
    --brand-blue: #0f6cb6;
    --sheet: #ffffff;
    --card: #f4f4f4;
    --muted: #b3b8c2;
    --caption: #9b9b9b;
    --mark-blue: #1672ba;
    --mark-purple: #8e2c86;
    --mark-orange: #ee8a24;
  }
  * { box-sizing: border-box; margin: 0; padding: 0; }
  html, body { width: 1200px; height: 1200px; overflow: hidden; }
  body { background: var(--frame-blue); font-family: "Source Sans 3", sans-serif; }
  .sheet {
    position: absolute; left: 19px; top: 19px; width: 1162px; height: 1162px;
    background: var(--sheet);
  }
  .caption {
    position: absolute; left: 0; top: 88px; width: 100%;
    text-align: center; color: var(--caption);
    font-weight: 300; font-size: 21px; line-height: 27.5px;
  }
  .card {
    position: absolute; left: 309px; top: 246px; width: 542px; height: 835px;
    background: var(--card);
    box-shadow: 3px 4px 8px rgba(0,0,0,0.22);
  }
  .brand-mark {
    position: absolute; left: 62px; top: 62px; width: 300px; height: 178px;
    background: linear-gradient(90deg, var(--mark-blue), var(--mark-purple) 50%, var(--mark-orange));
    opacity: 0.85;
  }
  .brand-name {
    position: absolute; left: 191px; top: 234px;
    font-family: "Roboto Condensed", sans-serif; font-weight: 700;
    font-size: 66px; line-height: 1; color: var(--brand-blue); letter-spacing: -0.5px;
  }
  .brand-trade {
    position: absolute; left: 192px; top: 305px;
    font-family: "Roboto Condensed", sans-serif; font-weight: 700;
    font-size: 30px; line-height: 1; color: var(--muted); letter-spacing: 0.3px;
  }
  .brand-claim {
    position: absolute; left: 192px; top: 342px;
    font-weight: 300; font-size: 25px; line-height: 1; color: var(--muted);
  }
  .person { position: absolute; left: 192px; top: 427px; }
  .person-name { font-size: 23px; font-weight: 400; color: var(--brand-blue); line-height: 24px; }
  .person-role { font-size: 22px; font-weight: 300; color: var(--muted); line-height: 24px; }
  .contact {
    position: absolute; left: 154px; list-style: none;
    font-size: 19px; font-weight: 600; color: var(--muted); line-height: 26.5px;
  }
  .contact li { display: flex; align-items: flex-start; }
  .contact .icon { width: 22px; height: 20px; margin: 3px 16px 0 0; flex: none; fill: var(--muted); }
  .contact .noicon { width: 38px; flex: none; }
  .contact .web { color: var(--brand-blue); }
  .contact-address { top: 540px; }
  .contact-phone { top: 619px; }
  .contact-online { top: 724px; }
</style>
</head>
<body>
<main class="sheet">
  <p class="caption">Farbraum<br>Visitenkarte Entwurf 01<br>Standard 85 x 55 mm<br>einseitig 4c &nbsp;|&nbsp; hochkant</p>

  <section class="card">
    <div class="brand-mark" role="img" aria-label="Platz für die farbige Pinselstrich-Bildmarke"></div>
    <div class="brand-name">FarbRaum</div>
    <div class="brand-trade">MALERMEISTERBETRIEB</div>
    <div class="brand-claim">Altes erhalten | Neues gestalten</div>

    <div class="person">
      <div class="person-name">Jonas Beispiel</div>
      <div class="person-role">Malermeister</div>
    </div>

    <ul class="contact contact-address">
      <li><svg class="icon" viewBox="0 0 22 20"><path d="M11 1 1 10h3v9h5v-6h4v6h5v-9h3z"/></svg>Farbweg 12</li>
      <li><span class="noicon"></span>54321 Beispielstadt</li>
    </ul>

    <ul class="contact contact-phone">
      <li><svg class="icon" viewBox="0 0 22 20"><path d="M4 1l4 4-2 3c1 3 4 6 7 7l3-2 4 4-3 3C9 19 2 12 1 4z"/></svg>01234 - 567 80</li>
      <li><svg class="icon" viewBox="0 0 22 20"><path d="M6 1h10v5H6zM2 7h18v8h-3v-3H5v3H2zM6 13h10v6H6z"/></svg>01234 - 567 81</li>
      <li><svg class="icon" viewBox="0 0 22 20"><path d="M7 0h8a1 1 0 0 1 1 1v18a1 1 0 0 1-1 1H7a1 1 0 0 1-1-1V1a1 1 0 0 1 1-1zm1 2v13h6V2zm3 14a1 1 0 1 0 0 2 1 1 0 0 0 0-2z"/></svg>0151 - 234 56 78</li>
    </ul>

    <ul class="contact contact-online">
      <li><svg class="icon" viewBox="0 0 22 20"><path d="M1 3h20v2l-10 6L1 5zM1 7l10 6 10-6v10H1z"/></svg>info@farbraum-maler.de</li>
      <li><svg class="icon" viewBox="0 0 22 20"><circle cx="11" cy="10" r="9"/><path d="M6 5c2 1 3 3 2 5s1 3 2 5M15 3c-1 2 0 4 2 5s2 3 1 5" stroke="#f4f4f4" stroke-width="2" fill="none"/></svg><span class="web">www.farbraum-maler.de</span></li>
    </ul>
  </section>
</main>
</body>
</html>
```